Business Cards & Stationary for Broadcast Company

We are a satellite company launching a new exciting brand by the name of "Veloran". Veloran is a broadcasting solution provider that gives end-to-end solutions to TV channels and other content providers to deliver and distribute their content globally. Weather it be TV channels that need to be broadcasted in their local regions or internationally, or its collection of news from various locations, or even coverage of special sports or other events, we provide the technology and services to make that happen.
we need a design for business cards as our top priority but also require letterhead and envelope design as well.
Business card will include the following information
Name: Karim Dusoki
Designation: General Manager
Mobile (M): +92 333 4718206
+971 55 2486153 (UAE)
Direct (D): +92 213 6140392
Office (O): +92 213 6142510-14
Fax (F): +92 213 6140392
Email (E): karim@veloran-example.biz
Website: www.veloran-example.biz

```html
<!DOCTYPE html>
<html lang="en">
<head>
<meta charset="utf-8">
<title>Veloran Stationery</title>
<link href="https://fonts.googleapis.com/css2?family=Open+Sans:wght@400;600;700&display=swap" rel="stylesheet">
<style>
:root{
  --bg:#c9d9e3;
  --paper:#ffffff;
  --ink:#333a40;
  --muted:#6b7278;
  --red:#e71d25;
  --sky:#00b2ec;
  --lime:#a8cd3a;
  --navy:#0060a6;
  --edge:#dfe4e8;
}
*{margin:0;padding:0;box-sizing:border-box}
html,body{width:1200px;height:1071px;overflow:hidden}
body{background:var(--bg);font-family:"Open Sans",Arial,sans-serif;color:var(--ink);position:relative}
.sheet{position:absolute;background:var(--paper);border:1px solid var(--edge)}
.letterhead{left:144px;top:72px;width:413px;height:562px}
.brand-mark{display:flex;align-items:center;gap:5px;font-weight:600;color:var(--ink)}
.brand-dot{width:9px;height:9px;border-radius:50%;background:var(--sky)}
.letterhead .brand-mark{position:absolute;top:40px;left:0;right:0;justify-content:center;font-size:13px}
.letter-title{position:absolute;top:170px;left:0;right:0;text-align:center;font-size:15px;font-weight:400;letter-spacing:.3px}
.letter-body{position:absolute;top:211px;left:53px;width:308px;font-size:5.4px;line-height:11.2px;color:var(--muted);text-align:justify}
.signature{position:absolute;left:294px;top:348px;width:66px;height:18px;background:linear-gradient(90deg,#e8eaec,#d4d8dc);border-radius:3px}
.signer{position:absolute;left:292px;top:372px;font-size:5px;color:var(--muted)}
.letter-contact{position:absolute;left:53px;top:503px;font-size:4.6px;line-height:7.2px;color:var(--muted)}
.cover{left:659px;top:74px;width:413px;height:562px;overflow:hidden}
.cover-art{position:absolute;inset:0;background:
  radial-gradient(ellipse 80% 70% at 0% 55%, rgba(0,96,166,.35), transparent 60%),
  radial-gradient(ellipse 90% 80% at 10% 40%, rgba(168,205,58,.35), transparent 65%),
  radial-gradient(ellipse 100% 90% at 20% 25%, rgba(0,178,236,.35), transparent 70%),
  radial-gradient(ellipse 90% 100% at 60% 0%, rgba(231,29,37,.3), transparent 70%),
  var(--paper)}
.envelope{position:absolute;background:var(--paper);border:1px solid var(--edge)}
.env-front{left:470px;top:840px;width:476px;height:172px}
.env-back{left:240px;top:740px;width:476px;height:224px}
.env-back svg{position:absolute;inset:0}
.seal{position:absolute;left:453px;top:831px;width:62px;height:62px;border-radius:50%;background:var(--paper);border:1px solid var(--edge);display:flex;align-items:center;justify-content:center}
.seal span{width:28px;height:28px;border-radius:50%;background:var(--sky)}
.env-front .brand-mark{position:absolute;left:306px;top:124px;font-size:9px}
.env-details{position:absolute;left:369px;top:118px;font-size:4.6px;line-height:6.4px;color:var(--ink)}
.env-details b{font-weight:700}
.env-details .web{margin-top:6px}
</style>
</head>
<body>
<section class="sheet letterhead">
  <div class="brand-mark"><span class="brand-dot"></span>Veloran</div>
  <h1 class="letter-title">OUR MISSION</h1>
  <p class="letter-body">Lorem ipsum dolor sit amet, consectetur adipiscing elit. Donec orci purus, luctus vitae dignissim eu, iaculis sed purus. Vivamus faucibus, ipsum nec aliquet viverra, leo mauris condimentum ligula, sit amet sagittis enim ligula quis arcu. Nam egestas tortor id nisi porttitor mattis. In tortor ante, ultricies in suscipit a, tempus non massa. Vivamus et auctor mi. Fusce vel massa nulla. Phasellus nec eros mauris, et scelerisque orci. Donec malesuada orci vitae nulla accumsan porta a id massa. Quisque accumsan iaculis magna sit amet fringilla.</p>
  <div class="signature" role="img" aria-label="Handwritten signature"></div>
  <p class="signer">Lena Marsh, Co-Founder &amp; CEO</p>
  <p class="letter-contact">(912) 555-0187<br>mail@veloran-example.biz<br>veloran-example.biz</p>
</section>

<section class="sheet cover">
  <div class="cover-art" role="img" aria-label="Sweeping brand curves in red, sky blue, lime and navy"></div>
</section>

<section class="envelope env-front">
  <div class="brand-mark"><span class="brand-dot"></span>Veloran</div>
  <div class="env-details">
    <div><b>Name:</b> Karim Dusoki</div>
    <div><b>Designation:</b> General Manager</div>
    <div><b>Email (E):</b> karim@veloran-example.biz</div>
    <div class="web"><b>Website: www.veloran-example.biz</b></div>
  </div>
</section>

<section class="envelope env-back">
  <svg width="476" height="224" viewBox="0 0 476 224" aria-hidden="true">
    <path d="M6 0 L22 100 Q24 114 40 114 L436 114 Q452 114 454 100 L470 0" fill="none" stroke="#e2e6e9" stroke-width="1.5"/>
  </svg>
</section>
<div class="seal"><span></span></div>
</body>
</html>
```